Flyer-Design für Vermittlung von Betreuungskräften
Zielgruppe
Wir vermitteln Betreuungskräfte aus Osteuropa für pflegebedürftige Menschen in Deutschland. Dabei legen wir Wert auf Seriösität, Professionalität und fürsorgliche Beratung. Folglich sind unsere Zielgruppe ältere Menschen und vor allem deren Angehörige, die für ihre Herzensmenschen entscheiden, ob die Pflege daheim ermöglicht wird. Der Flyer soll Wärme und Freundlichkeit ausstrahlen.
Aufgabenstellung
Es soll ein Wiedererkennungswert zu unserer Homepage sein. In den Flyer sollen folgende Kriterien:
-> Vorne: Schönes Bild von unserer HP, unser Slogan: Für Menschen. Aus Leidenschaft. und unser Logo
Weitere Inhalte/Seiten:
-> Kontakt mit Bild der jew. Ansprechpartner: Ich freue mich auf Ihre Kontaktaufnahme!
-> über uns mit folgendem Text:
'Wenn ein Mensch im Familien- oder Bekanntenkreis pflegebedürftig wird, stehen Angehörige meist vor einer großen Herausforderung und vielen Fragen. Wir sind Ihr Ansprechpartner und haben das Anliegen, pflegebedürftigen Menschen mit einer osteuropäischen liebevollen Betreuungskraft den Verbleib im eigenen Zuhause zu ermöglichen. '
-> Aufgaben der Betreuungskraft
- Grundpflege
Hilfe bei der Körperpflege, An- und auskleiden, Toilettengänge, Unterstützung beim Aufstehen usw.
- Haushaltshilfe
Aufräumen, Staubsaugen, Wäsche waschen, Geschirr spülen und mehr
- Kochen und Ernährung
sorgt sich um das leibliche Wohl inkl. Einhaltung Ernährungspläne, einkaufen von Lebensmitteln
- soziale Betreuung
Schutz vor Vereinsamung, spazieren gehen, Ausflüge, Pflege von Hobbies, Begleitung bei Arztbesuchen
Gerne mit schönen Symbolen
-> Warum belanoxa? siehe Homepage anlehnend an: Sechs Gründe, die für uns sprechen
-> Vier Schritte zu Ihrer Betreuungskraft siehe Homepage
Schrift Trenda
www.belanoxa,de

```html
<!DOCTYPE html>
<html lang="de">
<head>
<meta charset="utf-8">
<title>Flyer – Ansprechpartner, Über uns, Aufgabenbereich</title>
<link rel="stylesheet" href="https://fonts.googleapis.com/css2?family=Kaushan+Script&family=Didact+Gothic&display=swap">
<style>
  :root {
    --bg: #f8e2e5;
    --card: #ffffff;
    --accent: #d02b35;
    --arc: #e58990;
    --heading: #4f4f51;
    --text: #333335;
  }
  * { box-sizing: border-box; margin: 0; padding: 0; }
  html, body { width: 1200px; height: 813px; overflow: hidden; background: var(--bg); }
  .canvas { position: relative; width: 1200px; height: 813px; overflow: hidden; background: var(--bg);
    font-family: "Didact Gothic", "Century Gothic", sans-serif; color: var(--text); }
  .arc { position: absolute; inset: 0; }
  .box { position: absolute; background: var(--card); border-radius: 15px; }
  .column-title { display: flex; align-items: center; justify-content: center;
    font-family: "Kaushan Script", cursive; font-size: 40px; color: var(--heading); height: 83px; }

  .contacts { left: 49px; top: 160px; width: 325px; height: 603px; }
  .contact { position: absolute; left: 16px; width: 310px; height: 134px; }
  .portrait-frame { position: absolute; left: 0; top: 0; width: 134px; height: 134px;
    border: 1.5px solid var(--accent); border-radius: 22px; }
  .portrait { position: absolute; left: 17px; top: 17px; width: 100px; height: 100px;
    border-radius: 50%; background: var(--accent); }
  .contact-text { position: absolute; left: 154px; top: 15px; font-size: 15.5px; line-height: 19px; }
  .contact-text p + p { margin-top: 19px; }

  .about { left: 445px; width: 319px; padding: 10px 11px 0; font-size: 21.5px; line-height: 25.6px; text-align: center; }
  .about .justify-end { text-align: justify; text-align-last: justify; }

  .task { left: 840px; width: 311px; height: 134px; padding: 10px 10px 0 10px; }
  .task-title { font-size: 15.5px; color: var(--accent); text-decoration: underline; text-underline-offset: 3px; }
  .task-text { margin-top: 18px; font-size: 15.5px; line-height: 19px; }
  .task-icon { position: absolute; right: 8px; top: 6px; width: 44px; height: 44px;
    fill: none; stroke: var(--accent); stroke-width: 2; stroke-linecap: round; stroke-linejoin: round; }
</style>
</head>
<body>
<main class="canvas">
  <svg class="arc" width="1200" height="813" viewBox="0 0 1200 813" aria-hidden="true">
    <circle cx="1033" cy="341" r="423" fill="none" stroke="var(--arc)" stroke-width="4.5"/>
  </svg>

  <div class="box column-title" style="left:49px;top:49px;width:319px;">Ansprechpartner</div>
  <div class="box column-title" style="left:445px;top:49px;width:319px;">Über uns</div>
  <div class="box column-title" style="left:840px;top:51px;width:311px;">Aufgabenbereich</div>

  <section class="box contacts">
    <div class="contact" style="top:16px;">
      <div class="portrait-frame"><div class="portrait" role="img" aria-label="Porträtfoto Ansprechpartner"></div></div>
      <div class="contact-text"><p>Hallo ich bin<br>Max Mustermann.</p><p>Ich freue mich auf Ihre<br>Kontaktaufnahme!</p></div>
    </div>
    <div class="contact" style="top:214px;">
      <div class="portrait-frame"><div class="portrait" role="img" aria-label="Porträtfoto Ansprechpartner"></div></div>
      <div class="contact-text"><p>Hallo ich bin<br>Max Mustermann.</p><p>Ich freue mich auf Ihre<br>Kontaktaufnahme!</p></div>
    </div>
    <div class="contact" style="top:416px;">
      <div class="portrait-frame"><div class="portrait" role="img" aria-label="Porträtfoto Ansprechpartner"></div></div>
      <div class="contact-text"><p>Hallo ich bin<br>Max Mustermann.</p><p>Ich freue mich auf Ihre<br>Kontaktaufnahme!</p></div>
    </div>
  </section>

  <section class="box about" style="top:161px;height:181px;">
    Wenn ein Mensch im<br>Familien- oder Bekanntenkreis<br>pflegebedürftig wird, stehen<br>Angehörige meist vor einer großen<br>Herausforderung und vielen<br>Fragen.
  </section>
  <section class="box about" style="top:382px;height:217px;">
    Wir sind Ihr Ansprechpartner<br>und haben das Anliegen,<br>pflegebedürftigen Menschen<br>mit einer osteuropäischen<br>
    <span class="justify-end" style="display:block;">liebevollen Betreuungskraft den</span>
    <span class="justify-end" style="display:block;">Verbleib im eigenen Zuhause zu</span>
    ermöglichen.
  </section>

  <article class="box task" style="top:161px;">
    <h3 class="task-title" style="font-weight:400;">Grundpflege</h3>
    <svg class="task-icon" viewBox="0 0 44 44" aria-hidden="true">
      <path d="M14 8v4M5 17h4M7 10l3 3M21 10l-3 3M7 24l3-3"/>
      <path d="M11 22a6 6 0 0 1 10-7"/>
      <path d="M14 36h22a6 6 0 0 0 0-12 9 9 0 0 0-17-2 7 7 0 0 0-5 14z"/>
    </svg>
    <p class="task-text">Hilfe bei der Körperpflege,<br>An- und auskleiden, Toilettengänge,<br>Unterstützung beim Aufstehen usw.</p>
  </article>

  <article class="box task" style="top:321px;">
    <h3 class="task-title" style="font-weight:400;">Haushaltshilfe</h3>
    <svg class="task-icon" viewBox="0 0 44 44" aria-hidden="true">
      <path d="M5 18h20l-2 22H8z"/>
      <path d="M8 18a7 7 0 0 1 14 0"/>
      <path d="M36 4l-8 24M24 28l8 3-2 9-10-3z"/>
    </svg>
    <p class="task-text">Aufräumen, Staubsaugen,<br>Wäsche waschen, Geschirr spülen<br>und mehr</p>
  </article>

  <article class="box task" style="top:481px;">
    <h3 class="task-title" style="font-weight:400;">Kochen und Ernährung</h3>
    <svg class="task-icon" viewBox="0 0 44 44" aria-hidden="true">
      <path d="M14 20a6 6 0 1 1 4-10 6 6 0 0 1 10 0 6 6 0 1 1 4 10v5H14z"/>
      <path d="M19 20v5M23 20v5M27 20v5"/>
      <path d="M8 40l30-14M36 40L6 26"/>
      <circle cx="38" cy="24" r="3"/><circle cx="6" cy="24" r="3"/>
    </svg>
    <p class="task-text">sorgt sich um das leibliche Wohl inkl.<br>Einhaltung Ernährungspläne, einkaufen<br>von Lebensmitteln</p>
  </article>

  <article class="box task" style="top:629px;">
    <h3 class="task-title" style="font-weight:400;">soziale Betreuung</h3>
    <svg class="task-icon" viewBox="0 0 44 44" aria-hidden="true" style="stroke-width:2.6;">
      <path d="M22 40L6 22a9 9 0 0 1 16-11 9 9 0 0 1 16 11z"/>
    </svg>
    <p class="task-text">Schutz vor Vereinsamung, spazieren gehen,<br>Ausflüge, Pflege von Hobbies, Begleitung<br>bei Arztbesuchen</p>
  </article>
</main>
</body>
</html>
```